Velmo BUSINESS CARD

Design an attention-grabbing business cards. Draw inspiration from the provided logo file. Please use the same font style as in the logo.
the back side of the card is for accent/decoration.

Contact Information for Business Card

PLEASE USE PROVIDED BUSINESS CARD SAMPLE

Other font styles liked:
• LUMETTE

Colors
EB3D1F
EC4F4E
F09395
F8D3D4
FCEDEE

Requirements
Must have
• RED, BLACK COLORS, SOLID BACK COLOR
Nice to have
• MAKE IT FANCY

```html
<!DOCTYPE html>
<html lang="en">
<head>
<meta charset="utf-8">
<title>Velmo Business Card</title>
<link rel="stylesheet" href="https://fonts.googleapis.com/css2?family=Orbitron:wght@500;700&family=Mulish:wght@400;600&display=swap">
<style>
  :root {
    --bg: #e9e7e4;
    --card-white: #ffffff;
    --ink: #1e1c1d;
    --red: #d21f2e;
    --text-light: #ffffff;
    --muted: #4a4748;
  }
  * { margin: 0; padding: 0; box-sizing: border-box; }
  html, body { width: 1200px; height: 900px; overflow: hidden; background: var(--bg); }
  .stage { position: relative; width: 1200px; height: 900px; }

  .card {
    position: absolute;
    left: 302px;
    width: 595px;
    height: 340px;
    background: var(--card-white);
    box-shadow: 0 10px 28px rgba(0,0,0,0.18);
    overflow: hidden;
  }
  .card--front { top: 60px; }
  .card--back { top: 480px; }

  /* Front */
  .brand-lockup {
    position: absolute;
    left: 95px; top: 118px;
    display: flex; align-items: flex-end; gap: 18px;
  }
  .brand-square { width: 86px; height: 86px; background: var(--ink); }
  .brand-text { display: flex; flex-direction: column; }
  .brand-name {
    font-family: 'Orbitron', sans-serif;
    font-weight: 700;
    font-size: 68px;
    letter-spacing: 4px;
    line-height: 0.9;
    color: var(--ink);
  }
  .brand-tagline {
    margin-top: 8px;
    font-family: 'Mulish', sans-serif;
    font-size: 13px;
    letter-spacing: 2.5px;
    color: var(--muted);
  }

  /* Back */
  .back-art { position: absolute; inset: 0; }
  .person {
    position: absolute; left: 34px; top: 46px;
  }
  .person-name {
    font-family: 'Orbitron', sans-serif;
    font-weight: 700;
    font-size: 25px;
    letter-spacing: 1.5px;
    color: var(--red);
  }
  .person-title {
    font-family: 'Mulish', sans-serif;
    font-size: 16px;
    color: var(--text-light);
    margin-top: 2px;
  }
  .contact-list {
    position: absolute; left: 40px; top: 140px;
    list-style: none;
    display: flex; flex-direction: column; gap: 18px;
  }
  .contact-item { display: flex; align-items: center; gap: 16px; }
  .contact-icon { width: 42px; height: 42px; flex: none; }
  .contact-lines {
    font-family: 'Mulish', sans-serif;
    font-weight: 600;
    font-size: 14.5px;
    line-height: 1.3;
    color: var(--text-light);
  }
  .back-mark {
    position: absolute; left: 400px; top: 70px;
    width: 160px; height: 160px;
    border: 14px solid var(--red);
    border-radius: 50%;
    display: flex; align-items: center; justify-content: center;
  }
  .back-mark-name {
    font-family: 'Orbitron', sans-serif;
    font-weight: 700;
    font-size: 24px;
    letter-spacing: 2px;
    color: var(--red);
  }
</style>
</head>
<body>
<main class="stage">

  <section class="card card--front">
    <div class="brand-lockup">
      <div class="brand-square"></div>
      <div class="brand-text">
        <span class="brand-name">VELMO</span>
        <span class="brand-tagline">MOVING GOODS FORWARD</span>
      </div>
    </div>
  </section>

  <section class="card card--back">
    <svg class="back-art" viewBox="0 0 595 340" width="595" height="340">
      <path d="M0 0 H268 Q362 150 380 340 H0 Z" fill="var(--red)"/>
      <path d="M0 0 H236 Q328 150 346 340 H0 Z" fill="var(--ink)"/>
    </svg>

    <div class="person">
      <div class="person-name">OWEN HALE</div>
      <div class="person-title">President</div>
    </div>

    <ul class="contact-list">
      <li class="contact-item">
        <svg class="contact-icon" viewBox="0 0 42 42">
          <circle cx="21" cy="21" r="21" fill="var(--red)"/>
          <path d="M14 13 c-2 2 -1 6 3 10 s8 5 10 3 l1.5-1.5 -4-3.5 -2 1.5 c-2-1-4-3-5-5 l1.5-2 -3.5-4 z" fill="#fff"/>
        </svg>
        <div class="contact-lines">Office: +555-210-4830<br>Cell: +555-210-4917</div>
      </li>
      <li class="contact-item">
        <svg class="contact-icon" viewBox="0 0 42 42">
          <circle cx="21" cy="21" r="21" fill="var(--red)"/>
          <path d="M11 20 L31 13 L24 31 L21 23 Z" fill="#fff"/>
        </svg>
        <div class="contact-lines">OHale@velmo-llc.com<br>www.Velmo-LLC.com</div>
      </li>
      <li class="contact-item">
        <svg class="contact-icon" viewBox="0 0 42 42">
          <circle cx="21" cy="21" r="21" fill="var(--red)"/>
          <path d="M11 21 L21 12 L31 21 H28 V30 H14 V21 Z" fill="#fff"/>
          <rect x="19" y="24" width="4" height="6" fill="var(--red)"/>
        </svg>
        <div class="contact-lines">1480 N.200 East.<br>Larkfield, OH, 45012</div>
      </li>
    </ul>

    <div class="back-mark">
      <span class="back-mark-name">VELMO</span>
    </div>
  </section>

</main>
</body>
</html>
```